Design an Advertisement for QTL Real Estate

Hi Freelancers!

We are after some design concepts for a billboard ad that will be on a MAJOR road.
The billboard will be 2.01m High by 2.91m Wide

We are a real estate agency our website is qtl.com.au (please check it out for ideas)

Predominately we want to advertise key services:
Sales, Property Management and Finance

The style of the NEW billboard - please take inspiration from
http://pixelmarrow.com/advertising/creative-art-direction-print-ads/

There are NO RULES for this ad, we want innovative, creative, inspirational, VIRAL ideas. make it AMAZING! Make it INSPIRATIONAL!
We want to get the customer to call us or go to our website

Our logo is attached.

Also is the image of where the ad will be placed to help understand the positioning.

```html
<!DOCTYPE html>
<html lang="en">
<head>
<meta charset="utf-8">
<title>QTL Real Estate Billboard</title>
<link rel="stylesheet" href="https://fonts.googleapis.com/css2?family=Montserrat:wght@500;700&display=swap">
<style>
  :root {
    --page-bg: #e9e9eb;
    --frame: #b9b9bd;
    --panel-center: #ffffff;
    --panel-edge: #c9c9cc;
    --ink: #3a3a3c;
    --brand: #2f5ea8;
    --door-light: #e4e4e6;
    --door-dark: #c4c4c8;
  }
  * { margin: 0; padding: 0; box-sizing: border-box; }
  html, body {
    width: 1200px;
    height: 1200px;
    overflow: hidden;
    background: var(--page-bg);
    font-family: "Montserrat", Arial, sans-serif;
  }
  .billboard {
    position: absolute;
    left: 50px;
    top: 199px;
    width: 1100px;
    height: 802px;
    border: 14px solid var(--frame);
    background: radial-gradient(ellipse 55% 60% at 50% 42%, var(--panel-center) 0%, #f1f1f2 45%, var(--panel-edge) 100%);
  }
  .headline {
    position: absolute;
    left: 106px;
    top: 216px;
    width: 290px;
    text-align: center;
    color: var(--ink);
    font-weight: 500;
    font-size: 40px;
    line-height: 1.38;
  }
  .headline strong { font-weight: 500; text-transform: uppercase; }
  .door {
    position: absolute;
    left: 405px;
    top: 81px;
    width: 256px;
    height: 612px;
    background: linear-gradient(90deg, var(--door-dark), var(--door-light) 30%, var(--door-light) 70%, var(--door-dark));
    border: 6px solid #d6d6d9;
  }
  .brand {
    position: absolute;
    right: 34px;
    top: 640px;
    text-align: center;
    color: var(--brand);
  }
  .brand-name {
    font-weight: 700;
    font-size: 30px;
    letter-spacing: 1px;
    text-transform: uppercase;
  }
  .brand-web {
    margin-top: 10px;
    font-weight: 500;
    font-size: 22px;
    color: var(--brand);
  }
</style>
</head>
<body>
  <main class="billboard">
    <p class="headline"><strong>Happiness</strong><br>is opening<br>the door of<br>your new<br>home.</p>
    <div class="door" role="img" aria-label="A plain white panelled interior door, closed"></div>
    <div class="brand">
      <div class="brand-name">QTL Real Estate</div>
      <div class="brand-web">www.qtl.com.au</div>
    </div>
  </main>
</body>
</html>
```